Innovative Inbox Lantern Pop ups

Overview:
We’re creating a library of popup templates for our Cartwell app, Inbox Lantern (https://inboxlantern.example/
). These templates will be available for store owners across all types of businesses to use right away.

Most popup templates online are generic boxes with text and a button. That’s exactly what we don’t want. We want you to create out-of-the-box, design-driven templates that are instantly eye-catching, memorable, and conversion-focused.

Think of these as blank canvases: your designs should be so creative that store owners from any niche (fashion, tech, food, fitness, etc.) can drop in their own text, titles, and images — and still stand out.

What to Design:

5 unique popup templates (desktop + mobile).

Must work for any type of business and support any headline/title.

Templates should be bold, unexpected, and visually differentiated from competitors like Voxle, Brindaro, Orvo, and Flickbanner.

Include clear CTA areas (sign up, shop now, claim discount, etc.).

Designs should be mobile-first but also adapt beautifully to desktop.

Creative Direction:

Avoid standard box layouts — think beyond the rectangle.

Explore gamification, storytelling, interactive feel.

Use bold typography, unusual shapes, layered visuals, playful patterns, or luxury minimalism — but always in a way that supports conversions.

These are templates, not ads, so keep the text editable and layout flexible.

Deliverables:

Source files (Figma, Adobe XD, or Sketch).

Editable layers so text/images can be swapped easily.

5 designs with both desktop and mobile versions.

Contest Details:

This is a ArtQuorum contest. Multiple designers will submit entries.

We’ll select 1 winner based on creativity, originality, and differentiation.

The winning designs will become part of our client-facing template library.

Tips for Winning:

Design for universality: any store should be able to use your template by swapping in their own title/offer.

Be bold, surprising, and innovative. If your design looks like a typical popup, it won’t win.

Think of a popup as a mini-experience — something users remember, not ignore.
Updates

Hello Designers,

We have revised the project requirements, as it appears the client is not achieving the expected results. Please note that this project is not for logo design but for creating Inbox Lantern pop-ups. I have uploaded a sample image to the project brief for your reference. Kindly focus on producing innovative designs and avoid copying the sample provided to prevent any copyright concerns.

If you have any questions regarding the project, please feel free to reach out to the client through the discussion board.

Requirements
Should not have
• This is NOT a Logo Design.

```html
<!DOCTYPE html>
<html lang="en">
<head>
<meta charset="utf-8">
<title>Inbox Lantern Popup Templates</title>
<link rel="stylesheet" href="https://fonts.googleapis.com/css2?family=Poppins:wght@400;500;600;700;800&family=Inter:wght@400;500&family=Kalam:wght@400&family=Kaushan+Script&family=Yellowtail&display=swap">
<style>
  :root {
    --page: #ffffff;
    --tomato: #e02424;
    --lime: #7cb82a;
    --charcoal: #2d2d2d;
    --coral: #ec3a3a;
    --sky: #5bc8f0;
    --sun: #ffe600;
    --tangerine: #f5a03c;
    --ink: #050505;
    --amber: #ffa63d;
    --scarlet: #e8303a;
    --leaf-green: #2b9a1e;
    --wood: #5a3622;
    --wood-dark: #3f2415;
    --sand: #f0c08e;
    --white: #ffffff;
    --black: #111111;
  }
  html, body {
    margin: 0;
    padding: 0;
    width: 1200px;
    height: 1091px;
    overflow: hidden;
    background: var(--page);
  }
  .board { display: block; width: 1200px; height: 1091px; }
  .display { font-family: "Poppins", sans-serif; }
  .ui { font-family: "Inter", sans-serif; }
  .hand { font-family: "Kalam", cursive; }
  .brush { font-family: "Kaushan Script", cursive; }
  .script { font-family: "Yellowtail", cursive; }
  .brand-name { font-family: "Poppins", sans-serif; font-weight: 600; fill: var(--white); }
</style>
</head>
<body>
<svg class="board" viewBox="0 0 1100 1000" xmlns="http://www.w3.org/2000/svg">
  <defs>
    <linearGradient id="flame" x1="0" y1="0" x2="1" y2="1">
      <stop offset="0" stop-color="var(--amber)"/>
      <stop offset="1" stop-color="var(--scarlet)"/>
    </linearGradient>
    <linearGradient id="woodgrain" x1="0" y1="0" x2="1" y2="1">
      <stop offset="0" stop-color="var(--wood)"/>
      <stop offset="1" stop-color="var(--wood-dark)"/>
    </linearGradient>
    <radialGradient id="bubble">
      <stop offset="0.55" stop-color="#f6c7c7"/>
      <stop offset="1" stop-color="#ffffff" stop-opacity="0.6"/>
    </radialGradient>
  </defs>

  <!-- Food popup -->
  <g class="popup popup-food">
    <ellipse cx="300" cy="280" rx="165" ry="138" fill="var(--lime)"/>
    <ellipse cx="288" cy="273" rx="172" ry="140" fill="var(--tomato)"/>
    <text class="display" x="287" y="250" text-anchor="middle" font-size="64" font-weight="600" fill="var(--white)">10% Off</text>
    <text class="display" x="287" y="280" text-anchor="middle" font-size="25" fill="var(--white)">New Customers</text>
    <rect x="203" y="300" width="165" height="30" fill="var(--white)"/>
    <text class="hand" x="285" y="320" text-anchor="middle" font-size="13" fill="var(--black)">Yes, Count me in</text>
    <rect x="203" y="339" width="165" height="30" fill="var(--lime)"/>
    <text class="hand" x="285" y="359" text-anchor="middle" font-size="13" fill="var(--white)">No, Thank You</text>
    <circle cx="145" cy="195" r="36" fill="url(#bubble)" role="img" aria-label="Burger icon"/>
    <circle cx="388" cy="158" r="36" fill="url(#bubble)" role="img" aria-label="Pizza slice icon"/>
    <circle cx="145" cy="360" r="38" fill="url(#bubble)" role="img" aria-label="Wrap icon"/>
    <circle cx="424" cy="350" r="36" fill="url(#bubble)" role="img" aria-label="Taco icon"/>
  </g>

  <!-- Splash popup -->
  <g class="popup popup-splash">
    <polygon fill="var(--sun)" points="655,115 664,148 684,122 680,156 708,140 692,168 725,162 700,182 732,190 700,200 722,222 690,215 700,245 675,225 668,258 656,228 640,255 638,222 612,240 624,210 596,210 620,192 596,178 626,168 608,142 638,152 640,120"/>
    <ellipse cx="740" cy="270" rx="142" ry="135" fill="var(--coral)"/>
    <path d="M890 120 C 930 220, 990 280, 965 360 C 950 410, 900 425, 860 410 L 835 220 C 860 190, 880 160, 890 120 Z" fill="var(--sky)"/>
    <ellipse cx="783" cy="330" rx="175" ry="120" fill="var(--charcoal)"/>
    <text class="brand-name" x="775" y="184" text-anchor="middle" font-size="15">Knotwork</text>
    <text class="display" x="680" y="302" font-size="66" font-weight="700" fill="var(--white)">15%</text>
    <text class="brush" x="834" y="296" font-size="34" fill="var(--sun)">off</text>
    <text class="brush" x="678" y="332" font-size="26" fill="var(--tangerine)">new customers</text>
    <rect x="680" y="342" width="193" height="34" rx="2" fill="var(--white)"/>
    <rect x="680" y="384" width="193" height="34" rx="2" fill="var(--sun)"/>
    <text class="display" x="776" y="405" text-anchor="middle" font-size="12" font-weight="500" fill="var(--black)">Sign up Now!</text>
  </g>

  <!-- Hexagon popup -->
  <g class="popup popup-hexagon">
    <path d="M262 533 Q277 525 292 533 L426 610 Q440 618 440 634 L440 786 Q440 802 426 810 L292 887 Q277 895 262 887 L128 810 Q113 802 113 786 L113 634 Q113 618 128 610 Z" fill="var(--ink)"/>
    <text class="brand-name" x="277" y="586" text-anchor="middle" font-size="14">Knotwork</text>
    <rect x="120" y="622" width="312" height="96" rx="2" fill="url(#flame)"/>
    <text class="ui" x="265" y="645" text-anchor="middle" font-size="18" fill="var(--white)">DON'T MISS OUT!</text>
    <text class="display" x="134" y="697" font-size="56" font-weight="700" fill="var(--white)">10% Off!</text>
    <rect x="188" y="737" width="178" height="31" rx="2" fill="var(--white)"/>
    <text class="ui" x="277" y="757" text-anchor="middle" font-size="13" font-weight="500" fill="var(--black)">Yes, Count me in</text>
    <rect x="188" y="779" width="178" height="32" rx="2" fill="url(#flame)"/>
    <text class="ui" x="277" y="800" text-anchor="middle" font-size="13" fill="var(--white)">No, Thank You</text>
    <text class="brand-name" x="277" y="857" text-anchor="middle" font-size="14">Knotwork</text>
  </g>

  <!-- Woodland popup -->
  <g class="popup popup-woodland">
    <path d="M625 566 Q625 558 633 558 L967 558 Q975 558 975 566 L975 614 L625 614 Z" fill="var(--leaf-green)"/>
    <text class="display" x="800" y="603" text-anchor="middle" font-size="40" font-weight="800" fill="var(--white)">SIGN UP NOW!</text>
    <path d="M625 618 L975 618 L975 852 Q975 860 967 860 L633 860 Q625 860 625 852 Z" fill="url(#woodgrain)" role="img" aria-label="Dark wood plank texture"/>
    <text class="display" x="800" y="675" text-anchor="middle" font-size="40" font-weight="600" fill="var(--white)">10% OFF</text>
    <text class="script" x="800" y="704" text-anchor="middle" font-size="25" fill="var(--white)">for new customers only!</text>
    <rect x="662" y="718" width="274" height="48" rx="3" fill="var(--white)"/>
    <rect x="662" y="778" width="274" height="48" rx="3" fill="var(--sand)"/>
    <text class="display" x="799" y="809" text-anchor="middle" font-size="17" font-weight="500" fill="var(--black)">Subscribe now</text>
    <circle cx="975" cy="668" r="33" fill="var(--white)"/>
    <circle cx="977" cy="670" r="20" fill="var(--leaf-green)" role="img" aria-label="Tree icon"/>
    <circle cx="620" cy="800" r="35" fill="var(--white)"/>
    <circle cx="610" cy="802" r="20" fill="var(--leaf-green)" role="img" aria-label="Leaf icon"/>
  </g>
</svg>
</body>
</html>
```